依頼詳細
PCとスマホデザインの両方納品をいただきますが、
まずはデザインイメージが確認しやすいPCページのみの提案をお願いします。
スマホページは当選者に納品時にお願いしたいと思います。
スマホサイズについて、表示は横幅375pxで作成し、
デザインデータは2倍の横幅750pxのカンバスサイズで作成してください。
(Retinaディスプレイに対応するため)
レスポンシブウェブデザインを意識したデザインでお願いします。

■サイトマップ
添付の画面遷移図をご確認ください。

■参考サイト
http://www.kurumito.or.jp/

■内容について
以下のサイトのリニューアルになります。
https://e-sorana.jp/

■素材写真
画像データについては、フリー素材から流用して
イメージ画像に当て込んでください。
足りない場合は、一旦他のサイトの写真をサンプルとして
入れてください。(サンプルなどの表記をお願いします)
また、購入が必要な写真などを利用した場合、
価格とサイト名を教えてください。

また、Pixmoor Bankで定期契約をしていますので、
Pixmoor Bankの画像は使用できます。
デザイン時はカンプ画像をお入れいただきますようお願いします。

■ワイヤーフレーム
https://view.plotmesa.com/share/83f41a07-c2e9-4d1b-bb72-5e0a9f7d26c3-4a17/?fullscreen
コンテンツの構成としてワイヤーフレームを作成しましたが
必ずしもワイヤーフレームの通りではなくて大丈夫です。
TOPページに配置するコンテンツを見ていただき、デザインは
デザイナーの皆様におまかせしたいと思います。

----------------------------------------------------------------------------
【制作物に対するお願い】

■フォントについて
・無料で使えるフォントで作成をお願いします。
・OSに紐づくフォントの使用は控えていただければと思います (ヒラギノなど)

■その他
色味やデザインの雰囲気は添付のパンフレットを参考にしてください。
添付のパンフレットの色味
上記のいずれか1つ(アウトラインありとなしの2つ)と高解像度JPGを納品お願いします。
adobe XDでの納品も可能です。

クライアントのイメージ通りでした。

たくさんのご提案ありがとうございました。
次回もぜひ、よろしくお願い致します。

```html
<!DOCTYPE html>
<html lang="ja">
<head>
<meta charset="utf-8">
<title>みずほ市ひだまり育成会</title>
<link rel="stylesheet" href="https://fonts.googleapis.com/css2?family=Zen+Maru+Gothic:wght@400;500;700&display=swap">
<style>
:root{
  --green:#8cc63f;
  --green-dark:#6fa82a;
  --green-pale:#c9e39a;
  --text:#4d4d4d;
  --sub:#888;
  --bg:#fdfaf6;
  --pink:#fbe3e3;
  --blue:#e3f0f7;
  --line:#e6e0d8;
  --white:#fff;
}
*{margin:0;padding:0;box-sizing:border-box}
html,body{width:1200px;height:2840px;overflow:hidden}
body{background:var(--bg);color:var(--text);font-family:"Zen Maru Gothic",sans-serif;position:relative}
.abs{position:absolute}
/* header */
.site-header{position:absolute;top:0;left:0;width:1200px;height:70px}
.brand{left:40px;top:22px}
.brand small{display:block;font-size:10px;color:var(--green-dark)}
.brand strong{font-size:20px;color:var(--green-dark);font-weight:700;letter-spacing:.05em}
.global-nav{right:40px;top:22px;display:flex;align-items:center;gap:26px;font-size:13px}
.btn{display:inline-flex;align-items:center;gap:10px;background:var(--green);color:var(--white);border-radius:30px;font-weight:500}
.btn .dot{width:18px;height:18px;border-radius:50%;background:var(--white);display:inline-flex;align-items:center;justify-content:center}
.btn-sm{padding:7px 18px 7px 8px;font-size:12px}
.link{display:inline-flex;align-items:center;gap:10px;font-size:12px;color:var(--text)}
.link .dot{width:26px;height:26px;border-radius:50%;background:var(--green);display:inline-flex;align-items:center;justify-content:center}
/* hero */
.circle{position:absolute;border-radius:50%}
.hero-photo{left:110px;top:70px;width:970px;height:420px;border-radius:60px 260px 60px 200px/60px 200px 60px 160px;background:linear-gradient(180deg,#dfeef0 0%,#c9dfb8 45%,#a9c98c 100%)}
.mark{left:584px;top:510px;width:32px;height:32px;border-radius:50%;background:var(--green-pale)}
.catch{left:0;top:572px;width:1200px;text-align:center;font-size:28px;line-height:1.6;letter-spacing:.12em;font-weight:500}
/* sections */
.sec-title{font-size:26px;line-height:1.55;color:var(--green-dark);font-weight:700;letter-spacing:.06em}
.body-text{font-size:12px;line-height:2.1;color:var(--text)}
.vtext{writing-mode:vertical-rl;font-size:13px;letter-spacing:.15em;line-height:1.7}
.photo{border-radius:40px}
.photo-about{left:600px;top:770px;width:400px;height:250px;background:linear-gradient(135deg,#f4ece2,#e6d8c8 60%,#d9e6cf)}
.photo-service{left:200px;top:1250px;width:390px;height:250px;background:linear-gradient(135deg,#e9eef2,#f4e4dc 55%,#dfe9d4)}
.news-title{left:0;top:1610px;width:1200px;text-align:center;font-size:20px;font-weight:700;letter-spacing:.1em}
.news-list{left:270px;top:1665px;width:660px;list-style:none}
.news-list li{display:flex;gap:26px;border-bottom:1px solid var(--line);padding:11px 0;font-size:11.5px}
.news-list time{color:var(--green-dark);width:80px;flex:none}
.contact{left:130px;top:2020px;width:940px;height:270px;background:var(--white);border-radius:50px;box-shadow:0 6px 30px rgba(0,0,0,.04)}
.contact h2{position:absolute;top:40px;left:0;width:100%;text-align:center;color:var(--green-dark);font-size:20px;letter-spacing:.1em}
.contact p.lead{position:absolute;top:74px;left:0;width:100%;text-align:center;font-size:11px;color:var(--sub)}
.tel{position:absolute;left:120px;top:140px;font-size:40px;font-weight:700;letter-spacing:.03em;display:flex;align-items:center;gap:10px}
.tel-note{position:absolute;left:160px;top:196px;font-size:10px;color:var(--sub)}
.btn-lg{position:absolute;left:520px;top:140px;width:310px;height:70px;padding-left:14px;font-size:19px}
.btn-lg .dot{width:42px;height:42px}
/* footer */
.grass{left:0;top:2380px;width:1200px;height:460px}
.footer-box{left:100px;top:2560px;width:1000px;height:210px;background:var(--white);border-radius:8px}
.footer-brand small{display:block;font-size:10px;color:var(--green-dark)}
.footer-brand strong{font-size:20px;color:var(--green-dark)}
.footer-info{font-size:10px;line-height:1.9}
.footer-nav{font-size:11px;line-height:2.3;list-style:none}
.badge{width:150px;height:60px;border:1px solid var(--line);border-radius:4px;background:#f6f6f6}
.copy{left:0;top:2800px;width:1200px;text-align:center;font-size:10px;color:var(--white)}
</style>
</head>
<body>

<header class="site-header">
  <div class="abs brand"><small>社会福祉法人</small><strong>みずほ市ひだまり育成会</strong></div>
  <nav class="abs global-nav">
    <span>ひだまり育成会について</span><span>事業内容</span><span>設立案内</span>
    <span class="btn btn-sm"><span class="dot"><svg width="10" height="10" viewBox="0 0 10 10"><path d="M1 3h8v5H1z M1 3l4 3 4-3" fill="none" stroke="#8cc63f" stroke-width="1.2"/></svg></span>お問い合わせ</span>
  </nav>
</header>

<div class="circle" style="left:40px;top:150px;width:140px;height:140px;background:var(--blue)"></div>
<div class="circle" style="left:1010px;top:70px;width:200px;height:200px;background:var(--pink)"></div>
<div class="circle" style="left:1040px;top:330px;width:140px;height:140px;background:var(--blue)"></div>
<div class="abs hero-photo" role="img" aria-label="公園の並木道で手をつないで歩く家族の写真"></div>
<div class="abs mark"></div>
<p class="abs catch">一人ひとりの想いを尊重し<br>大切に育みます</p>

<!-- about -->
<div class="circle" style="left:520px;top:760px;width:120px;height:120px;background:var(--pink)"></div>
<h2 class="abs sec-title" style="left:125px;top:780px">障がい者のあたりまえを<br>社会のあたりまえに</h2>
<p class="abs body-text" style="left:125px;top:880px;width:400px">ひだまり育成会は、障がいのある人たちが地域の中で安心して暮らせるよう、本人や家族の想いに寄り添いながら、さまざまな活動と支援を続けています。<br><br>テキストテキストテキストテキストテキストテキストテキスト<br>テキストテキストテキスト</p>
<a class="abs link" style="left:330px;top:1062px"><span class="dot"><svg width="10" height="10" viewBox="0 0 10 10"><path d="M3 2l3 3-3 3" fill="none" stroke="#fff" stroke-width="1.5"/></svg></span>ひだまり育成会について</a>
<div class="abs photo photo-about" role="img" aria-label="室内で笑顔で話す家族と職員の写真"></div>
<div class="abs vtext" style="left:1040px;top:770px">ひだまり育成会<br>について</div>

<!-- service -->
<div class="circle" style="left:560px;top:1430px;width:120px;height:120px;background:var(--blue)"></div>
<div class="abs vtext" style="left:140px;top:1250px">事業内容</div>
<div class="abs photo photo-service" role="img" aria-label="色紙で折り紙を折る作業の手元の写真"></div>
<h2 class="abs sec-title" style="left:680px;top:1270px;font-size:24px">一人ひとりの個性・意思を尊重<br>サポートします</h2>
<p class="abs body-text" style="left:680px;top:1355px;width:400px">テキストテキストテキストテキストテキストテキストテキスト<br>テキストテキストテキスト<br><br>テキストテキストテキストテキストテキストテキストテキスト<br>テキストテキストテキスト</p>
<a class="abs link" style="left:910px;top:1510px"><span class="dot"><svg width="10" height="10" viewBox="0 0 10 10"><path d="M3 2l3 3-3 3" fill="none" stroke="#fff" stroke-width="1.5"/></svg></span>事業内容へ</a>

<!-- news -->
<h2 class="abs news-title">お知らせ</h2>
<ul class="abs news-list">
  <li><time>2020.00.00</time>新型感染症対策のため、定例会の開催を延期いたします。詳細はお知らせをご確認ください</li>
  <li><time>2020.00.00</time>ひだまり育成会だより 令和2年「事業所の紹介」を掲載しました</li>
  <li><time>2020.00.00</time>ひだまり育成会だより 令和2年「活動報告」を掲載しました</li>
  <li><time>2020.00.00</time>ひだまり作業所 ボランティア募集のお知らせ</li>
  <li><time>2020.00.00</time>社会福祉法人ひだまり育成会 事業報告書</li>
</ul>
<a class="abs link" style="left:860px;top:1915px"><span class="dot"><svg width="10" height="10" viewBox="0 0 10 10"><path d="M3 2l3 3-3 3" fill="none" stroke="#fff" stroke-width="1.5"/></svg></span>お知らせ一覧</a>

<!-- contact -->
<section class="abs contact">
  <h2>お問い合わせ</h2>
  <p class="lead">ご質問などございましたら、お気軽にお問い合わせください。</p>
  <div class="tel"><svg width="34" height="34" viewBox="0 0 24 24"><path d="M6.6 10.8a15 15 0 006.6 6.6l2.2-2.2a1 1 0 011-.25 11.4 11.4 0 003.6.57 1 1 0 011 1V20a1 1 0 01-1 1A17 17 0 013 4a1 1 0 011-1h3.5a1 1 0 011 1c0 1.25.2 2.45.57 3.6a1 1 0 01-.25 1z" fill="#4d4d4d"/></svg>0120-38-5274</div>
  <p class="tel-note">受付時間：平日 9:00〜17:00（土日祝を除く）</p>
  <span class="btn btn-lg"><span class="dot"><svg width="18" height="14" viewBox="0 0 18 14"><path d="M1 1h16v12H1z M1 1l8 6 8-6" fill="none" stroke="#8cc63f" stroke-width="1.6"/></svg></span>お問い合わせフォーム</span>
</section>

<!-- footer -->
<svg class="abs grass" viewBox="0 0 1200 460" preserveAspectRatio="none">
  <path d="M0 60 Q300 0 600 40 T1200 30 V460 H0z" fill="#c9e39a"/>
  <path d="M0 110 Q350 60 700 100 T1200 90 V460 H0z" fill="#a9d26a"/>
</svg>
<footer class="abs footer-box">
  <div class="abs footer-brand" style="left:30px;top:30px"><small>社会福祉法人</small><strong>みずほ市ひだまり育成会</strong></div>
  <p class="abs footer-info" style="left:30px;top:95px">〒000-0000<br>みずほ県みずほ市ひだまり町1-2-3<br>ひだまりサポートセンター内<br>TEL 0120-38-5274<br>FAX 0120-38-5275</p>
  <ul class="abs footer-nav" style="left:460px;top:30px"><li>ひだまり育成会について</li><li>事業内容</li><li>設立案内</li></ul>
  <ul class="abs footer-nav" style="left:660px;top:30px"><li>お知らせ</li><li>プライバシーポリシー</li><li>サイトマップ</li></ul>
  <div class="abs badge" style="left:820px;top:35px"></div>
</footer>
<p class="abs copy">Copyright © ひだまり育成会 All Rights Reserved.</p>

</body>
</html>
```